Crust Harbor Hotel Coupon

Would like to design a coupon that is for hotels' staff and to be dropped off at the hotel front office anytime someone calls from a hotel and as a Thank You for hotel staff for recommending us. Coupon value to be $ 2.00. Should say Thank You or Thank you for recommending us. Need our phone number 250 614 3750 on it. Color scheme to be Green and Red as in the attached logo. Coupon to be designed for printing size 3.5 inches high and 7.5 inches wide. Rear should say Fastest Delivery, Favourite Pizza for Sports teams etc. Ask for group deals. Attached logo to be on the coupon. Coupon should say coupon # and space left for us write number

```html
<!DOCTYPE html>
<html lang="en">
<head>
<meta charset="utf-8">
<title>Crust Harbor Hotel Coupon</title>
<link rel="stylesheet" href="https://fonts.googleapis.com/css2?family=Arvo:wght@400;700&display=swap">
<style>
  :root {
    --stage: #2b2b2b;
    --front-bg: #ececec;
    --back-bg: #f4f2ee;
    --green: #0f8a3c;
    --red: #d4202a;
    --ink: #1a1a1a;
    --crust: #d9923e;
    --sauce: #c8331f;
    --board: #e4e0d8;
  }
  * { box-sizing: border-box; margin: 0; padding: 0; }
  html, body {
    width: 1200px; height: 1200px; overflow: hidden;
    background: var(--stage);
    font-family: "Arvo", Georgia, serif;
  }
  .canvas { position: relative; width: 1200px; height: 1200px; }

  .coupon { position: absolute; left: 70px; width: 1060px; overflow: hidden; }
  .coupon--front { top: 68px; height: 512px; background: var(--front-bg); }
  .coupon--back  { top: 605px; height: 513px; }

  .brand {
    position: absolute;
    display: flex; align-items: center; gap: 14px;
    font-weight: 700; font-size: 48px; color: var(--green); line-height: 1;
    white-space: nowrap;
  }
  .brand__dot { width: 26px; height: 26px; border-radius: 50%; background: var(--red); flex: none; }
  .coupon--front .brand { top: 70px; left: 122px; }
  .coupon--back .brand  { top: 70px; left: 122px; }

  .front__photo {
    position: absolute; left: 672px; top: 0; width: 388px; height: 512px;
    background: radial-gradient(circle at 75% 25%, var(--sauce) 0 38%, var(--crust) 52%, transparent 66%),
                linear-gradient(180deg, #f0eeec, #e2dfdc);
  }
  .front__thanks {
    position: absolute; left: 77px; top: 178px;
    font-weight: 700; font-size: 100px; color: var(--green); letter-spacing: 2px; line-height: 1;
    white-space: nowrap;
  }
  .front__value {
    position: absolute; left: 77px; top: 282px;
    font-weight: 700; font-size: 106px; color: var(--red); letter-spacing: 4px; line-height: 1;
    white-space: nowrap;
  }
  .front__next {
    position: absolute; left: 77px; top: 400px;
    font-weight: 700; font-size: 27px; color: var(--red); line-height: 1.2;
  }
  .front__note {
    position: absolute; left: 78px; top: 440px;
    font-size: 19px; color: var(--ink); letter-spacing: 0.5px; line-height: 1.2;
  }

  .back__board {
    position: absolute; inset: 0;
    background: linear-gradient(180deg, var(--back-bg), var(--board));
  }
  .back__photo { position: absolute; }
  .back__photo--top {
    left: 795px; top: 0; width: 265px; height: 217px;
    background: radial-gradient(circle at 70% 30%, var(--sauce) 0 45%, var(--crust) 60%, transparent 75%);
  }
  .back__photo--bottom {
    left: 528px; top: 328px; width: 488px; height: 185px;
    background: radial-gradient(ellipse at 50% 75%, var(--sauce) 0 42%, var(--crust) 58%, transparent 72%);
  }
  .back__photo--left {
    left: 0; top: 160px; width: 45px; height: 290px;
    background: linear-gradient(90deg, var(--crust), transparent);
  }
  .back__photo--tomatoes {
    left: 330px; top: 0; width: 190px; height: 60px;
    background: radial-gradient(ellipse at 50% 30%, #c9261c 0 35%, transparent 65%);
  }
  .back__phone {
    position: absolute; left: 440px; top: 128px;
    font-weight: 700; font-size: 52px; color: var(--green); letter-spacing: 4px; line-height: 1.2;
    white-space: nowrap;
  }
  .back__perks { position: absolute; left: 153px; top: 225px; list-style: none; }
  .back__perks li {
    font-weight: 700; font-size: 25px; color: var(--red); letter-spacing: 0.6px;
    height: 45px; line-height: 1.2; white-space: nowrap;
  }
  .back__coupon {
    position: absolute; left: 153px; top: 408px;
    font-weight: 700; font-size: 25px; color: var(--red); line-height: 1.2; white-space: nowrap;
  }
</style>
</head>
<body>
<main class="canvas">
  <section class="coupon coupon--front">
    <div class="front__photo" role="img" aria-label="Pepperoni pizza with a hand lifting a slice"></div>
    <div class="brand"><span class="brand__dot"></span>Crust Harbor</div>
    <h1 class="front__thanks">Thank You!</h1>
    <p class="front__value">$2.00 Off</p>
    <p class="front__next">Your Next Order!</p>
    <p class="front__note">See other side for details.</p>
  </section>

  <section class="coupon coupon--back">
    <div class="back__board" role="img" aria-label="White wooden table with pizzas, tomatoes and herbs"></div>
    <div class="back__photo back__photo--tomatoes" role="img" aria-label="Cherry tomatoes"></div>
    <div class="back__photo back__photo--top" role="img" aria-label="Sliced pizza with arugula"></div>
    <div class="back__photo back__photo--left" role="img" aria-label="Edge of a pizza"></div>
    <div class="back__photo back__photo--bottom" role="img" aria-label="Vegetable pizza with peppers and mushrooms"></div>
    <div class="brand"><span class="brand__dot"></span>Crust Harbor</div>
    <p class="back__phone">250 614 3750</p>
    <ul class="back__perks">
      <li>Fastest Delivery.</li>
      <li>Favourite Pizza for Sports teams.</li>
      <li>Ask for group deals.</li>
    </ul>
    <p class="back__coupon">Coupon#_____________</p>
  </section>
</main>
</body>
</html>
```